Road Sign at our office 84 in X 48 in - Small Billboard

Kestrel Electrical
Electrical & Lighting Services

- we need a sign design for our small business/company based in Calhoun, GA called Kestrel Electrical - "our mission is to provide Northwest Georgia with dependable, high-quality electrical services that prioritize safety, integrity, and long-term reliability. As a woman-owned business with over 25 years of experience, we are committed to delivering exceptional workmanship and personalized service for every commercial, residential, and industrial project we undertake. We stand behind our work with a lifetime warranty—because your trust is our most powerful connection."

display logo, phone number, and open to other ideas without being cluttered, maybe instead of full website address, just use @ksrelectrical and it will send them to all of our website and socials...

it needs to be easy to read as they drive down the road
this is a place where people may be traveling at high speeds, make sure it's easy to see and understand at a glance.
It will be hanging 20-24ft from the ground. Like a small billboard.

https://ksrelectricworks.com/

Industry/Entity Type

Electrical Contractor

Requirements
Nice to have
• match the look and feel of website and socials

```html
<!DOCTYPE html>
<html lang="en">
<head>
<meta charset="UTF-8">
<title>Kestrel Electrical – Road Sign</title>
<link href="https://fonts.googleapis.com/css2?family=Montserrat:wght@600;700;800&display=swap" rel="stylesheet">
<style>
  :root {
    --ink: #111111;
    --charcoal: #2b2b2b;
    --flame-red: #f0623a;
    --flame-amber: #f7982f;
    --pill: #ff6a00;
    --paper: #ffffff;
    --backdrop: #e9e9e9;
  }
  * { box-sizing: border-box; margin: 0; padding: 0; }
  html, body {
    width: 925px; height: 1200px; overflow: hidden;
    background: var(--backdrop);
    font-family: "Montserrat", Arial, sans-serif;
  }
  .billboard {
    position: absolute; left: 20px; top: 348px;
    width: 885px; height: 504px;
    background: var(--paper);
    overflow: hidden;
  }
  .side-panel { position: absolute; inset: 0; width: 885px; height: 504px; }
  .brand {
    position: absolute; left: 58px; top: 70px;
    display: flex; align-items: center; gap: 14px;
  }
  .brand-dot {
    width: 30px; height: 30px; border-radius: 50%;
    background: var(--flame-amber);
  }
  .brand-name {
    font-weight: 800; font-size: 38px; color: var(--charcoal);
    letter-spacing: -0.5px;
  }
  .services, .sectors {
    position: absolute; top: 186px;
    font-weight: 800; font-size: 28px; line-height: 31px;
    text-transform: uppercase;
  }
  .services { left: 56px; color: var(--ink); }
  .sectors { left: 362px; }
  .sectors .accent { color: var(--flame-red); }
  .sectors .plain { color: var(--charcoal); }
  .pill {
    position: absolute; top: 306px; height: 50px;
    border-radius: 25px; background: var(--pill);
    color: var(--paper); font-weight: 800; font-size: 30px;
    display: flex; align-items: center; gap: 10px;
    padding-left: 20px;
  }
  .pill-phone { left: 44px; width: 289px; }
  .pill-social { left: 350px; width: 281px; padding-left: 24px; }
  .pill-icon { width: 20px; height: 20px; flex: none; }
  .warranty {
    position: absolute; left: 54px; top: 391px;
    font-weight: 800; font-size: 38px; letter-spacing: 4px;
    color: var(--ink);
  }
  .experience {
    position: absolute; left: 664px; top: 410px; width: 185px;
    text-align: center; font-weight: 800; text-transform: uppercase;
  }
  .experience .years { color: var(--flame-amber); font-size: 30px; line-height: 32px; }
  .experience .label { color: var(--paper); font-size: 21px; letter-spacing: 2px; line-height: 26px; }
</style>
</head>
<body>
  <section class="billboard">
    <svg class="side-panel" viewBox="0 0 885 504" aria-hidden="true">
      <defs>
        <linearGradient id="flameTone" x1="0" y1="0" x2="0" y2="1">
          <stop offset="0" stop-color="#f0623a"/>
          <stop offset="1" stop-color="#f7982f"/>
        </linearGradient>
      </defs>
      <path fill="var(--ink)" d="M600,0 H885 V504 H615 C610,440 650,390 700,340 C750,290 770,250 760,200 C740,120 660,60 600,0 Z"/>
    </svg>
    <svg class="side-panel" viewBox="0 0 885 504" role="img" aria-label="Flame swoosh decoration in red and amber">
      <path fill="url(#flameTone)" d="M480,0 H600 C660,60 740,120 760,200 C770,250 750,290 700,340 C650,390 610,440 615,504 H590 C585,440 620,380 670,330 C720,280 735,240 720,205 C680,130 560,90 480,0 Z"/>
    </svg>

    <div class="brand">
      <span class="brand-dot"></span>
      <span class="brand-name">Kestrel Electrical</span>
    </div>

    <div class="services">Electrical<br>&amp; Lighting<br>Services</div>
    <div class="sectors">
      <div class="accent">Commercial</div>
      <div class="plain">Residential</div>
      <div class="accent">Industrial</div>
    </div>

    <div class="pill pill-phone">
      <svg class="pill-icon" viewBox="0 0 24 24" aria-hidden="true">
        <path fill="#fff" d="M6.6 10.8c1.4 2.8 3.8 5.1 6.6 6.6l2.2-2.2c.3-.3.7-.4 1-.2 1.1.4 2.3.6 3.6.6.6 0 1 .4 1 1V20c0 .6-.4 1-1 1C10.6 21 3 13.4 3 4c0-.6.4-1 1-1h3.5c.6 0 1 .4 1 1 0 1.3.2 2.5.6 3.6.1.3 0 .7-.2 1L6.6 10.8z"/>
      </svg>
      <span>706-555-0148</span>
    </div>
    <div class="pill pill-social">
      <svg class="pill-icon" viewBox="0 0 24 24" aria-hidden="true">
        <circle cx="12" cy="12" r="9" fill="none" stroke="#fff" stroke-width="2.5"/>
      </svg>
      <span>ksrelectrical</span>
    </div>

    <div class="warranty">LIFETIME WARRANTY</div>

    <div class="experience">
      <div class="years">25+ Years</div>
      <div class="label">Experience</div>
    </div>
  </section>
</body>
</html>
```